Brightfern Systems Business Cards

We need a new business card design for an Electrical company that also focuses on Audio Visual and Communications. We would like to see designs using our new company logo attached. The cards are for two different people outlined below. Full contact details will be provided when design winner is awarded, use generic information for now. Business card is to be double sided and we are open to layout and design ideas.

Target Market(s)

Residential & Commercial

Industry/Entity Type

Electrical

Contact Information for Business Card

Name: Corwin Bell - Senior Electrician, Name: Milo Grant - Technology Specialist.

Font styles to use
Sans Serif

Colors
0555a3
ffffff
000000

Requirements
Must have
• mobile number, email address, website address, PO Box address,
• A main heading somewhere on the card stating ELECTRICAL SERVICES - AUDIO VISUAL SALES & INSTALLATION - COMMUNICATIONS

```html
<!DOCTYPE html>
<html lang="en">
<head>
<meta charset="utf-8">
<title>Brightfern Systems Business Card</title>
<link rel="stylesheet" href="https://fonts.googleapis.com/css2?family=Josefin+Sans:wght@600;700&family=Open+Sans:wght@400;600&display=swap">
<style>
  :root {
    --page: #fbf9fa;
    --brand-blue: #072c9c;
    --brand-blue-deep: #06288f;
    --white: #ffffff;
    --shadow: rgba(0, 0, 0, 0.45);
  }
  * { margin: 0; padding: 0; box-sizing: border-box; }
  html, body {
    width: 1200px; height: 840px; overflow: hidden;
    background: var(--page);
  }
  .canvas { position: relative; width: 1200px; height: 840px; }

  .card {
    position: absolute; left: 276px; width: 629px; height: 368px;
    box-shadow: 4px 5px 6px var(--shadow);
    overflow: hidden;
  }

  /* Front */
  .card--front { top: 28px; background: var(--brand-blue); }
  .front-brand {
    position: absolute; left: 0; right: 0; top: 98px;
    display: flex; flex-direction: column; align-items: center; gap: 22px;
  }
  .brand-dot { width: 86px; height: 86px; border-radius: 50%; background: var(--white); }
  .brand-name {
    font-family: "Josefin Sans", sans-serif; font-weight: 700;
    color: var(--white); text-align: center; letter-spacing: 1px;
    font-size: 40px; line-height: 1.05;
  }
  .services {
    position: absolute; left: 0; right: 0; bottom: 34px; text-align: center;
    font-family: "Open Sans", sans-serif; font-weight: 600; font-size: 11px;
    letter-spacing: 1px; color: var(--white);
  }

  /* Back */
  .card--back { top: 430px; background: var(--white); }
  .back-band {
    position: absolute; left: 0; right: 0; top: 183px; bottom: 0;
    background: var(--brand-blue);
  }
  .holder {
    position: absolute; right: 47px; top: 118px; text-align: right;
  }
  .holder-name {
    font-family: "Josefin Sans", sans-serif; font-weight: 700;
    font-size: 38px; line-height: 40px; letter-spacing: 1px; color: var(--brand-blue);
  }
  .holder-title {
    font-family: "Open Sans", sans-serif; font-size: 14px; line-height: 20px;
    color: var(--brand-blue);
  }
  .back-brand {
    position: absolute; left: 64px; top: 2px; width: 148px; height: 106px;
    background: var(--brand-blue-deep);
    display: flex; flex-direction: column; align-items: center; justify-content: center; gap: 8px;
  }
  .back-brand .brand-dot { width: 38px; height: 38px; }
  .back-brand .brand-name { font-size: 17px; letter-spacing: 0.5px; }

  .contact-list {
    position: absolute; left: 242px; top: 12px; list-style: none;
    font-family: "Open Sans", sans-serif; font-size: 18px; color: var(--white);
  }
  .contact-list li { display: flex; align-items: center; height: 25px; }
  .contact-icon {
    width: 20px; margin-right: 22px; display: flex; justify-content: center;
    font-size: 16px;
  }
  .contact-icon svg { width: 17px; height: 17px; fill: var(--white); }
  .address {
    position: absolute; left: 0; right: 0; top: 126px; text-align: center;
    font-family: "Open Sans", sans-serif; font-size: 14.5px; color: var(--white);
  }
</style>
</head>
<body>
<main class="canvas">
  <section class="card card--front" aria-label="Card front">
    <div class="front-brand">
      <span class="brand-dot"></span>
      <p class="brand-name">BRIGHTFERN<br>SYSTEMS</p>
    </div>
    <p class="services">ELECTRICAL SERVICES - AUDIO VISUAL SALES &amp; INSTALLATION - COMMUNICATIONS</p>
  </section>

  <section class="card card--back" aria-label="Card back">
    <div class="holder">
      <h1 class="holder-name">CORWIN BELL</h1>
      <p class="holder-title">Senior Electrician</p>
    </div>
    <div class="back-band">
      <div class="back-brand">
        <span class="brand-dot"></span>
        <p class="brand-name">BRIGHTFERN<br>SYSTEMS</p>
      </div>
      <ul class="contact-list">
        <li>
          <span class="contact-icon">
            <svg viewBox="0 0 24 24" aria-hidden="true"><path d="M3 9c0-3 4-5 9-5s9 2 9 5v2h-5V8.5c-1.3-.5-2.6-.7-4-.7s-2.7.2-4 .7V11H3z"/><path d="M7 12h10l3 7H4z"/></svg>
          </span>123-456-7890
        </li>
        <li><span class="contact-icon">@</span>corwin@brightfernsystems.com</li>
        <li>
          <span class="contact-icon">
            <svg viewBox="0 0 24 24" aria-hidden="true"><path d="M12 2a10 10 0 1 0 0 20 10 10 0 0 0 0-20zm-1 3c1 1-1 2 0 3s3 0 3 2-2 2-3 3 0 3-1 4-2-1-2-3-3-2-3-4 2-2 3-3 2-1 3-2zm5 9c1-1 3 0 3 1a8 8 0 0 1-3 3c-1-1-1-3 0-4z"/></svg>
          </span>www.brightfernsystems.com
        </li>
      </ul>
      <p class="address">Brightfern Systems PO Box XXX City city XXXXX</p>
    </div>
  </section>
</main>
</body>
</html>
```